Law Firm Website

I currently have a temporary site that I created myself at www.kbrandellegal.net (hosted by hostpivot). I am generally happy with the content.

My permanent website just has basic information right now: www.kbrandellegal.com (hosted by cloudperch). I want to take the general content from the temporary website and have a more professional looking website on the permanent website. I want it in Wordpress format. I want a link to my blog: www.rivetsand.com. I want it to work on pads and smart phones. My number and e-mail address should be available on every page. The idea is to feature the potential client more than the lawyer.
Updates

Several of the designs are good. I would like the front page to have my number and address at the top (and at the top of every page) and to identify my law firm as "Law Office of Karen J. Brandell". No need to include "kbrandellegal" as that is just the web address. I like showing the most recent blog posts on the front page. I don't need video. No need to emphasize office hours or map location on the front page (that could be under a contact button). My picture should be somewhere. I would like an image from Boston on the front page if we can find one that is not copyright protected. No images of gavels or scales of justice. See some of the sample websites I listed in previous messages. Thanks!

Reason: I need more time to evaluate designs.

Reason: Designers apparently misunderstood and provided design that was not wordpress.

Industry/Entity Type

Law Firm

```html
<!DOCTYPE html>
<html lang="en">
<head>
<meta charset="utf-8">
<title>Law Office of Karen J. Brandell</title>
<link rel="stylesheet" href="https://fonts.googleapis.com/css2?family=Quicksand:wght@400;500;600&family=Bebas+Neue&family=Arimo:wght@400;700&display=swap">
<style>
:root{
  --orange:#f07b10;
  --orange-dark:#d9650a;
  --ink:#000;
  --band:#0b0b0b;
  --band-box:#1c1c1c;
  --white:#fff;
  --paper:#f7f7f7;
  --line:#d6d6d6;
  --grey-text:#9a9a9a;
  --dark-text:#333;
}
*{margin:0;padding:0;box-sizing:border-box}
html,body{width:708px;height:1200px;overflow:hidden;background:var(--white)}
body{position:relative;font-family:Arimo,Arial,sans-serif;color:var(--dark-text)}

.hero{position:absolute;left:0;top:0;width:708px;height:287px}
.hero-photo{position:absolute;inset:0;background:linear-gradient(160deg,#3a3b3e 0%,#5c5d60 38%,#8a847c 60%,#4a3222 82%,#2a1a10 100%)}
.nav{position:absolute;left:51px;top:0;height:29px;display:flex;white-space:nowrap}
.nav a{display:block;color:var(--white);font-size:7.6px;text-decoration:none;line-height:29px;padding:0 7.5px;text-transform:uppercase;white-space:nowrap}
.nav a.current{background:var(--orange)}
.hero-title{position:absolute;left:0;width:708px;top:70px;text-align:center;font-family:Quicksand,sans-serif;font-weight:400;font-size:50px;color:var(--white);letter-spacing:1px;white-space:nowrap}
.hero-rule{position:absolute;left:165px;top:130px;width:380px;height:2px;background:var(--white)}
.hero-rule::before{content:"";position:absolute;left:0;top:-2px;width:50px;height:5px;background:var(--white)}
.hero-tag{position:absolute;left:0;width:708px;top:183px;text-align:center;font-family:"Bebas Neue",sans-serif;font-size:32px;color:#f5e6d8;letter-spacing:1px}

.cta-band{position:absolute;left:0;top:287px;width:708px;height:90px;background:var(--band)}
.cta-free{position:absolute;left:49px;top:16px;font-family:"Bebas Neue",sans-serif;font-size:31px;line-height:29px;color:var(--white);white-space:nowrap}
.cta-call{position:absolute;left:211px;top:23px;white-space:nowrap}
.cta-call .label{font-family:"Bebas Neue",sans-serif;font-size:15px;color:var(--orange);letter-spacing:.4px}
.cta-call .phone{font-family:"Bebas Neue",sans-serif;font-size:32px;color:var(--white);line-height:30px}
.cta-hours{position:absolute;left:374px;top:27px;font-size:9.5px;line-height:14px;color:var(--white);white-space:nowrap}
.chat-box{position:absolute;left:460px;top:0;width:197px;height:90px;background:var(--band-box)}
.chat-box .t{position:absolute;left:19px;top:16px;font-family:"Bebas Neue",sans-serif;font-size:29px;line-height:29px;color:var(--white);white-space:nowrap}
.chat-box .go{position:absolute;left:83px;top:18px;width:24px;height:20px;background:var(--orange)}

.services{position:absolute;left:0;top:377px;width:708px;height:163px;background:var(--white)}
.card{position:absolute;top:32px;width:141px;height:118px;border:1px solid var(--line);text-align:center;background:var(--white)}
.card .icon{position:absolute;left:63px;top:-10px}
.card h3{position:absolute;left:0;right:0;top:28px;font-family:Quicksand,sans-serif;font-weight:500;font-size:12.5px;line-height:16px;color:#333;text-transform:uppercase}
.btn{display:inline-block;background:var(--orange);color:var(--white);font-size:7px;text-transform:uppercase;text-decoration:none;padding:0 8px;line-height:21px}
.card .btn{position:absolute;left:34px;top:74px;width:63px;padding:0}

.blog-heading{position:absolute;left:0;width:708px;top:545px;text-align:center;font-family:Quicksand,sans-serif;font-weight:500;font-size:23px;color:var(--orange);letter-spacing:1px}

.blog{position:absolute;left:0;top:583px;width:708px;height:437px;background:linear-gradient(180deg,#000 0%,#0c0c0c 55%,#1b1b1b 80%,#050505 100%)}
.post{position:absolute;left:51px;width:376px}
.post .arrow{position:absolute;left:0;top:7px}
.post h2{margin-left:28px;font-family:Quicksand,sans-serif;font-weight:600;font-size:14px;line-height:16px;color:var(--orange)}
.post .meta{margin:5px 0 0 28px;font-size:7.5px;color:#ccc}
.post p{margin:9px 0 0 28px;font-size:8.6px;line-height:15.3px;color:#ddd}
.post .by{margin:6px 0 0 28px;font-size:7.5px;color:#ddd}

.signup{position:absolute;left:487px;top:603px;width:170px;height:226px;background:#d3d3d3;border:3px solid #555}
.signup h4{height:30px;background:var(--orange);color:var(--white);font-family:Quicksand,sans-serif;font-weight:600;font-size:13px;text-align:center;line-height:30px}
.signup .field{margin:8px 0 0 11px;width:142px;height:21px;background:var(--white);border:1px solid #bbb;font-size:7.5px;color:#888;padding-left:6px;line-height:19px}
.signup .btn{margin:8px 0 0 11px;width:68px;text-align:center}

.footer{position:absolute;left:0;top:1020px;width:708px;height:147px;background:var(--paper)}
.col{position:absolute;top:9px}
.col h5{font-family:Quicksand,sans-serif;font-weight:500;font-size:12.5px;color:var(--orange);margin-bottom:6px}
.col p{font-size:8px;line-height:15px;color:var(--grey-text)}
.col p.mail{color:var(--orange)}
.socials{display:flex;gap:5px;margin-top:5px}
.socials span{width:17px;height:17px;border-radius:50%;background:#c9c9c9}
.bottom-bar{position:absolute;left:0;top:1167px;width:708px;height:33px;background:var(--orange);color:var(--white);font-size:7.5px}
.bottom-bar .l{position:absolute;left:51px;top:12px}
.bottom-bar .r{position:absolute;right:51px;top:12px}
</style>
</head>
<body>

<header class="hero">
  <div class="hero-photo" role="img" aria-label="Photo of a lawyer in a dark suit signing documents at a wooden desk"></div>
  <nav class="nav">
    <a class="current" href="#">Home</a>
    <a href="#">Why hire me?</a>
    <a href="#">Success Stories</a>
    <a href="#">Practice Areas</a>
    <a href="#">Representative Clients</a>
    <a href="#">Services Provided</a>
    <a href="#">Contact Us</a>
    <a href="#">How to find us</a>
  </nav>
  <h1 class="hero-title">Karen J. Brandell</h1>
  <div class="hero-rule"></div>
  <div class="hero-tag">Law Agency</div>
</header>

<section class="cta-band">
  <div class="cta-free">Get Free Legal<br>Consultation:</div>
  <div class="cta-call">
    <div class="label">Call us toll free:</div>
    <div class="phone">617 555-0142</div>
  </div>
  <div class="cta-hours">7 days a week<br>from 8:00 am<br>to 2:00 am</div>
  <div class="chat-box">
    <div class="t">24/7<br>Our Support Chat</div>
    <div class="go"><svg width="24" height="20" viewBox="0 0 24 20"><path d="M10 5l6 5-6 5z" fill="#fff"/></svg></div>
  </div>
</section>

<section class="services">
  <div class="card" style="left:51px">
    <svg class="icon" width="14" height="17" viewBox="0 0 14 17"><circle cx="7" cy="4" r="3.5" fill="#333"/><path d="M1 17v-5c0-2 2-4 6-4s6 2 6 4v5z" fill="#333"/></svg>
    <h3>Protecting and<br>defending</h3>
    <a class="btn" href="#">Read more</a>
  </div>
  <div class="card" style="left:205px">
    <svg class="icon" width="14" height="17" viewBox="0 0 14 17"><circle cx="7" cy="4" r="3.5" fill="#333"/><path d="M1 17v-5c0-2 2-4 6-4s6 2 6 4v5z" fill="#333"/></svg>
    <h3>Rogue<br>employees</h3>
    <a class="btn" href="#">Read more</a>
  </div>
  <div class="card" style="left:360px">
    <svg class="icon" width="14" height="17" viewBox="0 0 14 17"><circle cx="7" cy="4" r="3.5" fill="#333"/><path d="M1 17v-5c0-2 2-4 6-4s6 2 6 4v5z" fill="#333"/></svg>
    <h3>Cheating<br>business partners</h3>
    <a class="btn" href="#">Read more</a>
  </div>
  <div class="card" style="left:516px">
    <svg class="icon" width="14" height="17" viewBox="0 0 14 17"><circle cx="7" cy="4" r="3.5" fill="#333"/><path d="M1 17v-5c0-2 2-4 6-4s6 2 6 4v5z" fill="#333"/></svg>
    <h3>Government<br>agencies</h3>
    <a class="btn" href="#">Read more</a>
  </div>
</section>

<h2 class="blog-heading">BLOG</h2>

<section class="blog">
  <article class="post" style="top:13px">
    <svg class="arrow" width="20" height="12" viewBox="0 0 20 12"><path d="M0 4h12V0l8 6-8 6V8H0z" fill="#fff"/></svg>
    <h2>You're Damned If You Don't Respond Appropriately to a Poor Rateline Review or Online Post.</h2>
    <div class="meta">Posted: January 15, 2014 in Lawsuits</div>
    <p>We live in crazy times for businesses. Any crackpot with a computer and internet connection can say anything that they want about your business in an online review, on social media, etc. That's the unfortunate reality for today's private businesses. The crackpots may even attack the business owner personally. Even worse, there is little you can do to stop it and, in many cases, you can't even get it removed (I won't bore you with a treatise on prior restraints of free speech). But do not take a defeatist attitude. Like getting sued, poor online reviews are now just a part of being a successful business. Below are some ideas on how to deal with them.</p>
    <div class="by">By Karen J. Brandell, 617.555.0142.</div>
  </article>
  <article class="post" style="top:221px">
    <svg class="arrow" width="20" height="12" viewBox="0 0 20 12"><path d="M0 4h12V0l8 6-8 6V8H0z" fill="#fff"/></svg>
    <h2>You're Damned If You Don't Respond Appropriately to a Poor Rateline Review or Online Post.</h2>
    <div class="meta">Posted: January 15, 2014 in Lawsuits</div>
    <p>We live in crazy times for businesses. Any crackpot with a computer and internet connection can say anything that they want about your business in an online review, on social media, etc. That's the unfortunate reality for today's private businesses. The crackpots may even attack the business owner personally. Even worse, there is little you can do to stop it and, in many cases, you can't even get it removed (I won't bore you with a treatise on prior restraints of free speech). But do not take a defeatist attitude. Like getting sued, poor online reviews are now just a part of being a successful business. Below are some ideas on how to deal with them.</p>
    <div class="by">By Karen J. Brandell, 617.555.0142.</div>
  </article>
</section>

<form class="signup">
  <h4>Complete to Begin</h4>
  <div class="field">First Name</div>
  <div class="field">Last Name</div>
  <div class="field">Phone No</div>
  <div class="field">E-Mail</div>
  <div class="field">Address</div>
  <div class="btn">Submit</div>
</form>

<footer class="footer">
  <div class="col" style="left:51px">
    <h5>Contact Us</h5>
    <p>Law Office of Karen J. Brandell<br>48 Alder St.<br>4th Floor<br>Boston, MA 02111<br>Phone: 617 555-0142<br>Fax: 857 555-0198</p>
    <p class="mail">Email: kbrandell@kbrandellegal.com</p>
  </div>
  <div class="col" style="left:284px">
    <h5>Office Hours</h5>
    <p>We can be reached during the<br>following hours:<br>Monday Thru Friday 10am-6pm</p>
  </div>
  <div class="col" style="left:517px">
    <h5>New Online Presentation</h5>
    <p>Under Construction<br>More news</p>
    <h5 style="margin-top:9px">Follow Us</h5>
    <div class="socials"><span></span><span></span><span></span><span></span></div>
  </div>
</footer>

<div class="bottom-bar">
  <span class="l">Copyright © 2014 Karen J. Brandell / All Reserved</span>
  <span class="r">Designed &amp; Developed by PixelForge Studio</span>
</div>

</body>
</html>
```